Corporate Web Redesign Project - coded

We would like redesign/refresh of our current site that would allow us to increase the depth of content and create a high quality impression for visitors.

Current site - http://corvanisystems.example/

A previous web redesign project has improved our site but it has not really reached the level we require.

Our customers are global, blue chip, organisations and a professional, corporate style of site is required.

Please note we would prefer a coded website to a just a design. We are happy to provide a zip of our current site if required.
Updates

                                   

Target Market(s)

Global oil and gas producers, KT, Pardo, Valmira etc.

Industry/Entity Type

It Professional

Requirements
Must have
• Design should support the level of content we currently have in the existing sitemap - although it should be expandable a site design for a large / complex site would not be appropriate

All current content / pages to be reflected in design

Must be visually appealing

Intuitive and clear navigation that is expandable

Display a high level of professionalism

Use a consistent palette of colours that complements our logo

Clean and organized layout

A way to capture visitor’s information or Call to action (i.e. contact link or form) on every page

Prominent Contact Information
Should not have
• Flash

```html
<!DOCTYPE html>
<html lang="en">
<head>
<meta charset="utf-8">
<title>Corvani Systems — The Business of Drilling Wells</title>
<link rel="stylesheet" href="https://fonts.googleapis.com/css2?family=Ubuntu:wght@400;500;700&family=Open+Sans:wght@400;600;700&display=swap">
<style>
:root{
  --teal-dark:#1d4f5c;
  --teal:#2a6677;
  --teal-mid:#3c7e8e;
  --ink:#1f5263;
  --text:#6d6d6d;
  --paper:#f1f0ec;
  --card:#fbfbfa;
  --news-bg:#dfe3e0;
  --footer:#1e1e1e;
  --footer-line:#3a3a3a;
  --field:#e9e9e9;
  --green:#7fa41a;
  --green-dark:#5f8410;
  --white:#ffffff;
  --muted:#8a8a8a;
}
*{box-sizing:border-box;margin:0;padding:0}
html,body{width:907px;height:1200px;overflow:hidden}
body{position:relative;background:var(--paper);font-family:"Open Sans",Arial,sans-serif;color:var(--text)}

/* top bar */
.top-bar{position:absolute;left:0;top:0;width:907px;height:18px;background:var(--teal-dark);
  color:#cfe0e4;font-size:8px;display:flex;justify-content:flex-end;align-items:center;gap:18px;padding-right:155px}
.top-bar span{display:flex;align-items:center;gap:4px}

/* header */
.site-header{position:absolute;left:0;top:18px;width:907px;height:51px;background:linear-gradient(#ffffff,#ececec)}
.brand{position:absolute;left:158px;top:13px;display:flex;align-items:center;gap:7px;
  font-family:"Ubuntu",sans-serif;font-weight:700;font-size:16px;color:var(--ink);text-transform:uppercase;letter-spacing:.5px}
.brand-dot{width:22px;height:22px;border-radius:50%;background:var(--teal-mid)}
.main-nav{position:absolute;left:415px;top:0;height:51px;display:flex}
.main-nav a{height:51px;padding:0 12px;display:flex;flex-direction:column;align-items:center;justify-content:flex-end;padding-bottom:9px;
  font-family:"Ubuntu",sans-serif;font-weight:700;font-size:10.5px;color:var(--ink);text-decoration:none;border-left:1px solid #d8d8d8;gap:5px}
.main-nav a i{width:11px;height:11px;border-radius:50%;background:var(--teal-mid);display:block}
.main-nav a.active{background:var(--teal);color:var(--white)}
.main-nav a.active i{background:var(--white)}

/* hero */
.hero{position:absolute;left:0;top:69px;width:907px;height:272px;
  background:radial-gradient(ellipse at 60% 45%,#8b9aa3 0%,#4d6675 35%,#2c4656 70%,#1d3240 100%)}
.hero-photo{position:absolute;left:400px;top:0;width:310px;height:272px;
  background:linear-gradient(180deg,rgba(200,210,215,.25),rgba(70,80,90,.45))}
.hero-copy{position:absolute;left:156px;top:72px;color:var(--white)}
.hero-copy h1{font-family:"Ubuntu",sans-serif;font-weight:700;font-size:30px;line-height:30px;text-transform:uppercase;letter-spacing:-.3px}
.hero-copy ul{list-style:none;margin-top:8px}
.hero-copy li{font-size:10px;line-height:18px;display:flex;align-items:center;gap:7px}
.hero-copy li::before{content:"";width:7px;height:7px;background:#9bc42a;border:1px solid #e6f2c8}
.hero-arrow{position:absolute;top:102px;width:26px;height:60px;display:flex;align-items:center;justify-content:center}
.hero-arrow.prev{left:105px}
.hero-arrow.next{left:771px;background:rgba(20,45,60,.75)}

/* section headings */
.section-title{position:absolute;left:0;width:907px;text-align:center;font-family:"Ubuntu",sans-serif;font-weight:700;
  font-size:15px;color:var(--ink);text-transform:uppercase;display:flex;justify-content:center;align-items:center;gap:6px}
.section-title .mark{width:18px;height:18px;border-radius:50%;background:var(--teal-mid)}
.title-rule{position:absolute;height:1px;background:#b8c6c9}

/* about */
.about-text{position:absolute;left:195px;top:425px;width:520px;text-align:center;font-size:9.3px;line-height:13px}
.services{position:absolute;left:157px;top:486px;display:flex;gap:7px}
.service-card{width:144px;height:106px;background:var(--card);box-shadow:0 1px 3px rgba(0,0,0,.15);text-align:center;padding-top:10px}
.service-icon{width:28px;height:28px;margin:0 auto;border-radius:50%}
.service-card h3{font-family:"Ubuntu",sans-serif;font-weight:700;font-size:11px;color:var(--ink);margin-top:7px}
.service-card p{font-size:8px;line-height:10px;padding:2px 14px 0}

/* news */
.news-box{position:absolute;left:216px;top:665px;width:475px;height:121px;background:var(--news-bg);border:1px solid #d3d8d6}
.news-thumb{position:absolute;left:28px;top:25px;width:65px;height:65px;background:var(--white);display:flex;align-items:center;justify-content:center}
.news-thumb span{width:24px;height:24px;border-radius:50%;background:var(--teal-mid)}
.news-box h4{position:absolute;left:105px;top:31px;font-family:"Ubuntu",sans-serif;font-weight:700;font-size:11px;color:var(--ink)}
.news-box p{position:absolute;left:105px;top:47px;width:355px;font-size:8.3px;line-height:10.5px}
.news-arrow{position:absolute;top:713px;width:11px;height:26px;display:flex;align-items:center;justify-content:center}
.news-arrow.prev{left:206px;background:var(--teal)}
.news-arrow.next{left:691px;background:var(--green)}

/* clients */
.clients{position:absolute;left:0;top:814px;width:907px;height:70px;background:var(--white);
  display:flex;justify-content:center;align-items:center;gap:42px}
.clients span{font-family:"Open Sans",sans-serif;font-weight:700;font-size:12px;color:#7b7b7b}

/* footer */
.site-footer{position:absolute;left:0;top:884px;width:907px;height:316px;background:var(--footer);color:var(--muted)}
.site-footer .section-title{color:var(--white);top:46px;font-size:14px}
.site-footer .section-title .mark{background:#cfcfcf}
.contact-form{position:absolute;left:157px;top:92px;width:278px}
.field-row{display:flex;gap:3px;margin-bottom:3px}
.field{flex:1;height:16px;background:var(--field);border-radius:2px;font-size:7px;color:#9a9a9a;padding:3px 5px}
.field.message{height:57px}
.send-btn{margin-top:3px;height:28px;border-radius:2px;background:linear-gradient(var(--green),var(--green-dark));
  color:var(--white);font-family:"Ubuntu",sans-serif;font-weight:700;font-size:14px;display:flex;align-items:center;justify-content:center;gap:6px}
.office{position:absolute;top:110px;width:130px;font-size:9px;line-height:12px}
.office h5{font-family:"Ubuntu",sans-serif;font-weight:700;font-size:10.5px;color:var(--white);margin-bottom:7px;text-transform:uppercase}
.office .line{display:flex;gap:6px;margin-bottom:4px}
.office .line svg{flex:none;margin-top:2px}
.office-divider{position:absolute;left:603px;top:98px;width:1px;height:100px;background:var(--footer-line)}
.footer-rule{position:absolute;left:157px;top:240px;width:595px;height:1px;background:var(--footer-line)}
.footer-links{position:absolute;left:157px;top:264px;font-size:7.5px;display:flex;gap:8px}
.copyright{position:absolute;left:157px;top:276px;font-size:7px}
.partner{position:absolute;left:598px;top:263px;width:155px;text-align:center}
.partner strong{display:block;font-family:"Ubuntu",sans-serif;font-weight:700;font-size:12.5px;color:var(--white);letter-spacing:.5px}
.partner small{font-size:6.5px}
</style>
</head>
<body>

<div class="top-bar">
  <span><svg width="9" height="7" viewBox="0 0 9 7"><rect x=".5" y=".5" width="8" height="6" fill="none" stroke="#cfe0e4"/><path d="M.5 .5l4 3 4-3" fill="none" stroke="#cfe0e4"/></svg>enquiries@corvanisystems.example</span>
  <span><svg width="8" height="8" viewBox="0 0 8 8"><path d="M1 1l2 0 1 2-1 1c.5 1 1 1.5 2 2l1-1 2 1v2C4 8 0 4 1 1z" fill="#cfe0e4"/></svg>(713) 555 0142</span>
</div>

<header class="site-header">
  <div class="brand"><span class="brand-dot"></span>Corvani Systems</div>
  <nav class="main-nav">
    <a class="active" href="#"><i></i>HOME</a>
    <a href="#"><i></i>NEWS</a>
    <a href="#"><i></i>ABOUT US</a>
    <a href="#"><i></i>SOLUTIONS</a>
    <a href="#"><i></i>CONTACT US</a>
  </nav>
</header>

<section class="hero">
  <div class="hero-photo" role="img" aria-label="Photograph of a semi-submersible offshore drilling rig against a blurred industrial background"></div>
  <div class="hero-copy">
    <h1>The Business of<br>Drilling Wells</h1>
    <ul>
      <li>Understand and communicate project cost and risk</li>
      <li>Control and reduce expenditure</li>
      <li>Learn and improve performance</li>
    </ul>
  </div>
  <div class="hero-arrow prev"><svg width="14" height="26" viewBox="0 0 14 26"><path d="M12 2L2 13l10 11" fill="none" stroke="#fff" stroke-width="2.5"/></svg></div>
  <div class="hero-arrow next"><svg width="14" height="26" viewBox="0 0 14 26"><path d="M2 2l10 11L2 24" fill="none" stroke="#fff" stroke-width="2.5"/></svg></div>
</section>

<h2 class="section-title" style="top:381px"><span class="mark"></span>About Us</h2>
<div class="title-rule" style="left:380px;top:407px;width:147px"></div>
<p class="about-text">From early phase evaluation through planning, execution and post analysis of wells, we deliver the tools, processes and people required to facilitate major performance improvement and cost savings. Our solutions are used in more than 30 countries to support operations ranging from a single well to global deployments with Major Operators.</p>

<div class="services">
  <div class="service-card">
    <div class="service-icon" role="img" aria-label="Clock icon" style="background:#7fa41a"></div>
    <h3>Time &amp; Cost Estimation</h3>
    <p>CXR delivers a standardized, systematic approach to understanding project risk.</p>
  </div>
  <div class="service-card">
    <div class="service-icon" role="img" aria-label="Gears icon" style="background:#3a78b5"></div>
    <h3>Materials &amp; Cost Control</h3>
    <p>CXM has been helping companies optimize materials and cost tracking processes since 1992.</p>
  </div>
  <div class="service-card">
    <div class="service-icon" role="img" aria-label="Test tubes icon" style="background:#d0503c"></div>
    <h3>Lessons Learned</h3>
    <p>CXL is an advanced lessons learned &amp; knowledge system for use in the energy industry.</p>
  </div>
  <div class="service-card">
    <div class="service-icon" role="img" aria-label="Consulting people icon" style="background:#e99a1c"></div>
    <h3>Services &amp; Consulting</h3>
    <p>Successful software implementations rely on people and processes to deliver results.</p>
  </div>
</div>

<h2 class="section-title" style="top:628px">Latest News</h2>
<div class="title-rule" style="left:357px;top:649px;width:193px"></div>

<div class="news-arrow prev"><svg width="5" height="8" viewBox="0 0 5 8"><path d="M4 0L0 4l4 4z" fill="#fff"/></svg></div>
<article class="news-box">
  <div class="news-thumb"><span></span></div>
  <h4>CXR Offset Data Mapper Assisting North Sea Estimates</h4>
  <p>The CXR Offset Data Mapper (ODM) is a platform for linking offset data sources, such as morning reporting databases, to CXR to facilitate cost estimates. Using the ODM facilitates fast, robust and auditable estimating with direct link to the relevant offset data.</p>
</article>
<div class="news-arrow next"><svg width="5" height="8" viewBox="0 0 5 8"><path d="M1 0l4 4-4 4z" fill="#fff"/></svg></div>

<div class="clients">
  <span>Valmira</span><span>Harrow</span><span>Sorrel</span><span>Kestrel</span><span>KT</span><span>Linmar</span><span>Tovan</span>
</div>

<footer class="site-footer">
  <h2 class="section-title"><span class="mark"></span>Get In Touch</h2>
  <div class="title-rule" style="left:370px;top:70px;width:167px;background:#444"></div>

  <form class="contact-form">
    <div class="field-row"><div class="field">First Name</div><div class="field">Last Name</div></div>
    <div class="field-row"><div class="field">Email</div><div class="field">Company</div></div>
    <div class="field-row"><div class="field message">Message</div></div>
    <div class="send-btn">SEND <svg width="14" height="12" viewBox="0 0 14 12"><path d="M0 6l14-6-3 12-4-3-2 3V8l7-6-8 5z" fill="#fff"/></svg></div>
  </form>

  <div class="office" style="left:480px">
    <h5>Europe</h5>
    <div class="line"><svg width="7" height="9" viewBox="0 0 7 9"><path d="M3.5 0A3.5 3.5 0 0 0 0 3.5C0 6 3.5 9 3.5 9S7 6 7 3.5A3.5 3.5 0 0 0 3.5 0z" fill="#777"/></svg><span>18 Marlow Row<br>Aberdeen<br>AB11 4QZ</span></div>
    <div class="line"><svg width="7" height="7" viewBox="0 0 8 8"><path d="M1 1l2 0 1 2-1 1c.5 1 1 1.5 2 2l1-1 2 1v2C4 8 0 4 1 1z" fill="#777"/></svg><span>+44(0)1224 555019</span></div>
    <div class="line"><svg width="8" height="6" viewBox="0 0 8 6"><rect width="8" height="6" fill="#777"/></svg><span>eu@corvanisystems.example</span></div>
  </div>
  <div class="office-divider"></div>
  <div class="office" style="left:631px">
    <h5>North America</h5>
    <div class="line"><svg width="7" height="9" viewBox="0 0 7 9"><path d="M3.5 0A3.5 3.5 0 0 0 0 3.5C0 6 3.5 9 3.5 9S7 6 7 3.5A3.5 3.5 0 0 0 3.5 0z" fill="#777"/></svg><span>4100 Westmere Pkwy<br>Suite 210<br>Houston, TX 77063</span></div>
    <div class="line"><svg width="7" height="7" viewBox="0 0 8 8"><path d="M1 1l2 0 1 2-1 1c.5 1 1 1.5 2 2l1-1 2 1v2C4 8 0 4 1 1z" fill="#777"/></svg><span>(713) 555 0142</span></div>
    <div class="line"><svg width="8" height="6" viewBox="0 0 8 6"><rect width="8" height="6" fill="#777"/></svg><span>us@corvanisystems.example</span></div>
  </div>

  <div class="footer-rule"></div>
  <nav class="footer-links"><span>Home</span><span>News</span><span>About Us</span><span>Solutions</span><span>Contact Us</span></nav>
  <p class="copyright">Copyright © Corvani Systems Ltd 2013</p>
  <div class="partner"><strong>NORTHGATE PARTNER</strong><small>Gold Independent Software Vendor (ISV)</small></div>
</footer>

</body>
</html>
```